Webdesign für Bau von Wohnanlagen aus Containermodulen
Zielgruppe
Wir bauen Wohnanlagen, Bürogebäude, Kindergärten, Schulen etc. aus einzelnen Containermodulen - übernehmen die Montage, Umbau und Versetzung, Reparaturen und Einlagerungen. Unsere Zielgruppe sind überwiegend Firmen und Kommunen. Der Text für die Homepage ist bereits fertig. Hier erhalten Sie weitere Informationen über unser Tätigkeitsfeld.
Aufgabenstellung
Die Farbe unseres Logos ist blau. Sie sollte sich natürlich in der Homepage minimal widerspiegeln, aber nicht dominieren. Bilder sollten nicht zu klein gehalten werden. Wir möchten dadurch zeigen, was möglich ist (z.B. Umsetzungen von ganzen Containeranlagen am Stück - hier haben wir eine Monopolstellung).

```html
<!DOCTYPE html>
<html lang="de">
<head>
<meta charset="utf-8">
<title>Kontakt – Kessler Montagearbeiten</title>
<link rel="stylesheet" href="https://fonts.googleapis.com/css2?family=Open+Sans:wght@400;600;700&family=Roboto+Slab:wght@300&display=swap">
<style>
:root{
  --brand:#0d2383;
  --text:#333333;
  --white:#ffffff;
  --panel:#eeeeee;
  --footer:#5f5f5f;
  --hero-a:#d9dfe4;
}
*{margin:0;padding:0;box-sizing:border-box}
html,body{width:1200px;height:930px;overflow:hidden}
body{position:relative;background:var(--white);font-family:"Open Sans",sans-serif;color:var(--text)}
.abs{position:absolute}
.site-header{left:0;top:0;width:1200px;height:94px;background:var(--white)}
.brand{left:232px;top:18px;height:64px;display:flex;align-items:center;gap:8px;color:var(--brand);font-weight:700;font-size:22px;letter-spacing:1px}
.brand-mark{width:18px;height:18px;background:var(--brand)}
.tagline{left:420px;top:14px;font-family:"Roboto Slab",serif;font-weight:300;font-size:16px;color:#444;white-space:nowrap}
.main-nav{left:0;top:71px;width:1200px;height:14px;font-size:10.5px}
.main-nav a{position:absolute;text-decoration:none;color:#333;white-space:nowrap}
.main-nav a.active{color:var(--brand);font-weight:700}
.hero{left:0;top:94px;width:1200px;height:308px;background:linear-gradient(90deg,#8f7a6a 0%,#c9ccd0 30%,var(--hero-a) 55%,#5d7ab0 75%,var(--hero-a) 100%)}
.breadcrumb{left:234px;top:411px;font-size:9px;letter-spacing:2px;color:#333;white-space:nowrap}
.breadcrumb b{font-weight:600;letter-spacing:0;margin-left:4px}
.page-title{left:232px;top:451px;font-size:20px;font-weight:400;color:var(--brand)}
.page-sub{left:232px;top:485px;font-size:11.5px;font-weight:700;color:var(--brand)}
.intro{left:232px;top:527px;width:740px;font-size:11.3px;line-height:19px}
.contact-band{left:0;top:621px;width:1200px;height:271px;background:var(--panel)}
.call-bar{left:232px;top:647px;width:735px;height:50px;background:var(--brand);color:var(--white)}
.call-text{left:15px;top:10px;width:500px;font-size:11.3px;line-height:15px;white-space:nowrap}
.call-phone{left:526px;top:0;height:50px;display:flex;align-items:center;gap:10px;font-size:22.5px;white-space:nowrap}
.form-title{left:230px;top:720px;font-size:20px;font-weight:400;color:var(--brand)}
.address{left:232px;top:752px;font-size:11.3px;line-height:19px;font-style:normal}
.field{background:var(--white);font-size:11.3px;color:#333;padding-left:11px;display:flex;align-items:center}
.field.msg{align-items:flex-start;padding-top:5px;padding-left:8px}
.send{left:860px;top:835px;width:107px;height:25px;background:var(--brand);color:var(--white);font-weight:700;font-size:11.3px;display:flex;align-items:center;justify-content:center}
.site-footer{left:0;top:892px;width:1200px;height:38px;background:var(--footer);color:var(--white);font-size:9px;letter-spacing:2px;padding:13px 0 0 232px;white-space:nowrap}
</style>
</head>
<body>
<header class="abs site-header">
  <div class="abs brand"><span class="brand-mark"></span>KESSLER</div>
  <div class="abs tagline">Ihr Partner für mobile Container</div>
  <nav class="abs main-nav">
    <a style="left:515px">HOME</a>
    <a style="left:571px">LEISTUNGEN</a>
    <a style="left:657px">WIR ÜBER UNS</a>
    <a style="left:755px">REFERENZEN</a>
    <a style="left:842px">AKTUELLES</a>
    <a class="active" style="left:921px">KONTAKT</a>
  </nav>
</header>

<div class="abs hero" role="img" aria-label="Foto: lächelnde Mitarbeiterin am Telefon in einem hellen Büro mit Laptop"></div>

<div class="abs breadcrumb">KESSLER MONTAGEARBEITEN &nbsp;» <b>Kontakt</b></div>
<h1 class="abs page-title">Kontakt</h1>
<h2 class="abs page-sub">Immer für Sie da</h2>
<p class="abs intro">Unser erfahrenes Team ist vom Erstkontakt bis zur Realisierung Ihres Projektes und darüber hinaus immer für Sie da. Ob per E-Mail, telefo-<br>nisch oder auch persönlich vor Ort –&nbsp; wir unterstützen Sie optimal bei der Umsetzung Ihres Vorhabens.</p>

<section class="abs contact-band"></section>
<div class="abs call-bar">
  <div class="abs call-text">Für sämtliche Anliegen oder Fragen in Zusammenhang mit unseren Dienstleistungen stehen<br>wir Ihnen jederzeit gerne zur Verfügung. Wir freuen uns auf Ihren Anruf.</div>
  <div class="abs call-phone">
    <svg width="22" height="22" viewBox="0 0 24 24" aria-hidden="true"><path fill="#fff" d="M6.6 10.8c1.4 2.8 3.8 5.1 6.6 6.6l2.2-2.2c.3-.3.7-.4 1-.2 1.1.4 2.3.6 3.6.6.6 0 1 .4 1 1V20c0 .6-.4 1-1 1C10.6 21 3 13.4 3 4c0-.6.4-1 1-1h3.5c.6 0 1 .4 1 1 0 1.3.2 2.5.6 3.6.1.3 0 .7-.2 1z"/></svg>
    <span>+49 7000-555120</span>
  </div>
</div>

<h2 class="abs form-title">Kontaktformular</h2>
<address class="abs address">Kessler Montagearbeiten<br>Lindenweg 12<br>70999 Talheim<br>Telefon: 07000-555120<br>Telefax: 07000-555121<br>E-Mail: info@kessler-montage.de</address>

<div class="abs field" style="left:484px;top:760px;width:232px;height:25px">Name *</div>
<div class="abs field" style="left:484px;top:798px;width:232px;height:25px">E-Mail-Adresse *</div>
<div class="abs field" style="left:484px;top:835px;width:232px;height:25px">Telefonnummer *</div>
<div class="abs field msg" style="left:735px;top:760px;width:232px;height:62px">Ihre Nachricht an uns</div>
<div class="abs send">absenden</div>

<footer class="abs site-footer">KESSLER MONTAGEARBEITEN &nbsp; | © 2017 &nbsp;| &nbsp; IMPRESSUM</footer>
</body>
</html>
```